New Business Card Design Project

We are a spa looking to create a professional elegant business card for a spa mainly black and white with a splash of lime green. This card will be two sided - the front side will have an image, the logo, and the spa's information - the back side will have a promotion for new customers - NEW CUSTOMERS $20 OFF

Look and feel: chic, modern, and spa-ish.
Information to be included:
Therapist Name
Therapist specialty
Address: 5174 Marlowe Ave, Beverly Hills CA 90211
Phone: (310) 482-3957

Let me know if you have any questions!

Thank you

Industry/Entity Type

Business

```html
<!DOCTYPE html>
<html lang="en">
<head>
<meta charset="utf-8">
<title>Lumen Day Spa – Business Card</title>
<link rel="stylesheet" href="https://fonts.googleapis.com/css2?family=Questrial&family=Archivo+Black&display=swap">
<style>
  :root {
    --backdrop: #d6d6d6;
    --card: #ffffff;
    --lime: #8cc63f;
    --lime-soft: #b9dc7c;
    --lime-pale: #eef6e0;
    --ink: #111111;
    --photo-light: #f4f4f4;
    --photo-mid: #d2d2d2;
    --photo-dark: #a9a9a9;
  }
  * { box-sizing: border-box; margin: 0; padding: 0; }
  html, body {
    width: 1200px; height: 900px; overflow: hidden;
    background: var(--backdrop);
    font-family: "Questrial", "Century Gothic", sans-serif;
    color: var(--ink);
  }
  .sheet {
    width: 1200px; height: 900px;
    display: flex; align-items: center; justify-content: center; gap: 40px;
  }
  .card {
    position: relative; width: 540px; height: 310px;
    border-radius: 28px; overflow: hidden;
    background: var(--card);
    box-shadow: 0 10px 24px rgba(0,0,0,0.18);
  }

  /* Front */
  .front-art { position: absolute; inset: 0; width: 540px; height: 310px; }
  .brand {
    position: absolute; left: 30px; top: 46px; width: 120px;
    text-align: center; font-size: 26px; line-height: 30px; color: var(--ink);
  }
  .brand span { display: block; }
  .therapist { position: absolute; right: 36px; top: 30px; }
  .therapist-name { font-size: 20px; line-height: 24px; color: var(--lime); }
  .therapist-specialty { font-size: 15px; line-height: 20px; color: var(--ink); }
  .contact {
    position: absolute; left: 24px; top: 222px;
    font-size: 16px; line-height: 21px; list-style: none;
  }
  .contact li { display: flex; align-items: flex-start; gap: 5px; }
  .contact svg { width: 14px; height: 14px; margin-top: 3px; flex: none; }
  .contact .indent { padding-left: 19px; }

  /* Back */
  .pattern {
    position: absolute; inset: 0;
    background: radial-gradient(ellipse at center, var(--lime-pale) 0%, var(--lime-soft) 70%, var(--lime) 140%);
  }
  .back-brand {
    position: absolute; left: 0; right: 0; top: 70px;
    text-align: center; font-size: 30px; line-height: 34px; color: #ffffff;
  }
  .back-brand span { display: block; }
  .promo {
    position: absolute; left: 0; right: 0; top: 176px;
    text-align: center;
    font-family: "Archivo Black", "Arial Black", sans-serif;
    font-size: 22px; letter-spacing: 5px; color: var(--ink);
  }
</style>
</head>
<body>
<main class="sheet">
  <section class="card card-front" aria-label="Card front">
    <svg class="front-art" viewBox="0 0 540 310" aria-hidden="false">
      <defs>
        <linearGradient id="photo-tone" x1="0" y1="0" x2="1" y2="0">
          <stop offset="0" stop-color="#ffffff"/>
          <stop offset="0.2" stop-color="var(--photo-light)"/>
          <stop offset="0.6" stop-color="var(--photo-mid)"/>
          <stop offset="1" stop-color="var(--photo-dark)"/>
        </linearGradient>
      </defs>
      <path role="img" aria-label="Black and white photo of a woman relaxing during a spa massage"
            d="M190 182 C250 176 290 168 330 158 C410 130 480 118 540 112 L540 310 L190 310 Z"
            fill="url(#photo-tone)"/>
      <path d="M0 148 C120 175 220 172 320 140 C410 112 480 100 540 96 L540 112 C480 118 410 130 330 158 C230 190 110 190 0 156 Z"
            fill="var(--lime)"/>
    </svg>
    <p class="brand"><span>Lumen</span><span>Day Spa</span></p>
    <div class="therapist">
      <p class="therapist-name">Therapist Name</p>
      <p class="therapist-specialty">Therapist specialty</p>
    </div>
    <ul class="contact">
      <li>
        <svg viewBox="0 0 24 24"><path fill="var(--lime)" d="M6.6 10.8a15.1 15.1 0 0 0 6.6 6.6l2.2-2.2c.3-.3.7-.4 1-.2 1.1.4 2.3.6 3.6.6.6 0 1 .4 1 1V20c0 .6-.4 1-1 1A17 17 0 0 1 3 4c0-.6.4-1 1-1h3.5c.6 0 1 .4 1 1 0 1.3.2 2.5.6 3.6.1.3 0 .7-.2 1z"/></svg>
        <span>(310) 482-3957</span>
      </li>
      <li>
        <svg viewBox="0 0 24 24"><path fill="var(--lime)" d="M12 3 2 12h3v8h5v-6h4v6h5v-8h3z"/></svg>
        <span>5174 Marlowe Ave,</span>
      </li>
      <li class="indent"><span>Beverly Hills CA 90211</span></li>
    </ul>
  </section>

  <section class="card card-back" aria-label="Card back">
    <div class="pattern" role="img" aria-label="Lime green leaf and swirl pattern on white"></div>
    <p class="back-brand"><span>Lumen</span><span>Day Spa</span></p>
    <p class="promo">NEW CUSTOMERS $20 OFF</p>
  </section>
</main>
</body>
</html>
```